Professional Single Page Website Design for Velloway Advisory

Velloway Advisory is a new business consultancy specializing in providing expert services to small businesses, primarily in the brick-and-mortar retail and food service sectors. We offer a range of services including franchise development and launch, due diligence, and construction management.

Currently, we have a basic website set up at www.vellowayadvisory.example, but we need a professional touch to enhance its design and functionality.

Project Requirements:
- Single Page Design: For now, we need a single page design that effectively showcases who we are, our services, and contact information.
- Future Expansion: The design should be flexible and scalable for future expansion to include additional pages like specific service offerings, about us, and a dedicated contact page.
- Design Aesthetic: We are looking for a modern yet professional design that aligns with our brand identity.
- Logo: We have a logo that we like, which was also sourced from Pixel Forum. The logo files are attached to this project brief.

Key Sections to Include:
- Hero Section: An engaging introduction to Velloway Advisory with a strong visual impact.
- About Us: A brief overview of who we are and our mission.
- Team: Section for the profiles of the two principals.
- Services: A clear and concise presentation of our services, including franchise development, due diligence, and construction management.
- Contact Information: Easy-to-find contact details, including a form for inquiries.
- Call to Action: Encouraging visitors to get in touch with us for consultations or further information.

Design Considerations:
- Ensure the design is responsive and mobile-friendly.
- Include high-quality images and icons that complement our services and industry.
- We do not need development services, this is only a design project.

```html
<!DOCTYPE html>
<html lang="en">
<head>
<meta charset="utf-8">
<title>Velloway Advisory</title>
<link href="https://fonts.googleapis.com/css2?family=Poppins:wght@400;500;600;700;800&display=swap" rel="stylesheet">
<style>
:root{
  --navy:#1d2833;
  --navy-deep:#15202b;
  --ink:#1b2b3c;
  --mint:#8fc9b1;
  --mint-soft:#e2f3ec;
  --teal:#5ea98a;
  --text:#3a4450;
  --white:#ffffff;
}
*{box-sizing:border-box;margin:0;padding:0}
html,body{width:1200px;height:3198px;overflow:hidden;background:#fff}
body{font-family:"Poppins",sans-serif;color:var(--text);position:relative}
.section{position:absolute;left:0;width:1200px}

/* HERO */
.hero{top:0;height:600px;background:var(--mint);border-bottom-right-radius:190px}
.hero-photo{position:absolute;inset:0 0 10px 0;border-bottom-right-radius:180px;
  background:linear-gradient(120deg,#1a2a3c 0%,#2c4258 35%,#4f6273 55%,#1c2a38 80%,#121c27 100%)}
.nav{position:absolute;top:26px;left:0;width:1200px;height:44px}
.brand{position:absolute;display:flex;align-items:center;gap:10px;color:var(--white);font-weight:600;font-size:17px}
.brand-dot{width:34px;height:34px;border-radius:50%;border:3px solid var(--mint)}
.nav .brand{left:150px;top:4px}
.nav-links{position:absolute;left:560px;top:12px;display:flex;gap:28px;font-size:13px;color:var(--white)}
.nav-links .active{border-bottom:2px solid var(--mint);padding-bottom:3px}
.btn-inquiry{position:absolute;left:943px;top:4px;width:108px;height:30px;background:var(--mint);color:var(--ink);
  font-size:12px;font-weight:600;display:flex;align-items:center;justify-content:center}
.hero-card{position:absolute;left:175px;top:150px;width:318px;height:316px;background:var(--mint);border-radius:36px;padding:48px 0 0 44px}
.hero-card h1{font-size:41px;line-height:44px;font-weight:800;color:var(--ink);letter-spacing:.5px}
.hero-card .sub{font-size:30px;line-height:36px;font-weight:400;color:var(--ink);margin-top:6px}
.hero-card .tag{font-size:12px;color:var(--ink);margin-top:10px}
.hero-card .tag b{display:block;font-size:13px;font-weight:600}

/* WHO WE ARE */
.who{top:600px;height:210px;text-align:center}
.eyebrow{color:var(--teal);font-weight:600;font-size:11px;letter-spacing:.5px;padding-top:80px}
.who p{width:760px;margin:6px auto 0;font-size:10.5px;line-height:16px;color:var(--text)}
.who hr{position:absolute;left:226px;bottom:0;width:778px;border:0;border-top:1px solid #e4e4e4}

/* ABOUT */
.about{top:810px;height:520px}
.about-mark{position:absolute;left:167px;top:78px;width:316px;height:316px;border-radius:50%;border:38px solid var(--mint)}
.about-name{position:absolute;left:167px;top:410px;width:316px;text-align:center;color:var(--mint);font-weight:600;font-size:20px}
.about-copy{position:absolute;left:539px;top:88px;width:510px}
.h2{color:var(--mint);font-weight:700;font-size:25px;letter-spacing:.5px}
.about-copy h3{color:var(--ink);font-size:13.5px;font-weight:600;line-height:18px;margin:8px 0 16px}
.about-copy p{font-size:10.5px;line-height:15.5px;margin-bottom:14px}

/* SERVICES */
.services{top:1330px;height:540px}
.services-band{position:absolute;left:0;top:30px;width:1200px;height:510px;background:var(--navy)}
.services-photo{position:absolute;left:688px;top:0;width:512px;height:540px;border-top-left-radius:150px;
  background:linear-gradient(160deg,#3a2550 0%,#2a2b45 40%,#6b4a32 70%,#2a2a2c 100%)}
.services-copy{position:absolute;left:150px;top:100px;width:465px}
.tabs{display:flex;gap:34px;margin-top:30px;border-bottom:1px solid #3c4956;padding-bottom:12px}
.tab{width:130px;font-size:11.5px;font-weight:500;line-height:15px;color:#8a96a2}
.tab.on{color:var(--mint);position:relative}
.tab.on:after{content:"";position:absolute;left:0;bottom:-13px;width:100px;height:2px;background:var(--mint)}
.icon-box{width:46px;height:44px;border-radius:6px;background:#6b7580;display:flex;align-items:center;justify-content:center;margin-bottom:10px}
.tab.on .icon-box{background:var(--mint)}
.services-copy p{font-size:10.5px;line-height:15.5px;color:#d7dde2;margin-top:26px}
.services-copy p + p{margin-top:14px}

/* TEAM */
.team{top:1870px;height:440px;background:var(--mint-soft)}
.team .h2{text-align:center;padding-top:72px}
.card{position:absolute;top:158px;width:433px;height:210px;background:#f4faf7;border-radius:20px;box-shadow:0 10px 18px rgba(0,0,0,.07)}
.card.one{left:155px}.card.two{left:612px}
.avatar{position:absolute;left:20px;top:0;width:158px;height:158px;border-radius:28px;background:linear-gradient(180deg,#c8c6c0 0%,#8a7a6c 55%,#2c2f36 100%)}
.card.two .avatar{background:linear-gradient(180deg,#b9cbd8 0%,#9a8a7c 55%,#e8ecef 100%)}
.card-body{position:absolute;left:198px;top:28px;width:205px}
.card-body h4{color:var(--ink);font-size:15px;font-weight:600}
.card-body .role{color:var(--mint);font-size:12px;margin-bottom:12px}
.card-body p{font-size:9.5px;line-height:15px}
.contact-icons{position:absolute;left:55px;top:174px;display:flex;gap:11px}
.ci{width:22px;height:22px;border-radius:50%;border:1px solid #333;display:flex;align-items:center;justify-content:center}
.ci.hot{background:var(--mint);border-color:var(--mint)}

/* CTA */
.cta{top:2310px;height:470px}
.cta-photo{position:absolute;left:222px;top:60px;width:316px;height:288px;border-top-right-radius:110px;
  background:linear-gradient(180deg,#5c92d2 0%,#8fb7e2 35%,#a6654a 65%,#6a8fa8 100%)}
.cta-copy{position:absolute;left:590px;top:130px;width:390px}
.cta-copy h2{color:var(--ink);font-size:24px;font-weight:700;line-height:31px;letter-spacing:.5px}
.cta-copy p{font-size:10.5px;line-height:15.5px;margin:14px 0 20px}
.btn-dark{display:inline-block;background:var(--navy);color:#fff;font-size:11px;font-weight:600;padding:8px 18px}

/* FOOTER */
.footer{top:2780px;height:418px;background:var(--mint);border-top-right-radius:150px}
.footer-inner{position:absolute;left:0;top:10px;width:1200px;height:408px;border-top-right-radius:140px;
  background:linear-gradient(135deg,#1f2b37 0%,#243342 55%,#1a2530 100%)}
.footer .brand{left:490px;top:56px;font-size:22px}
.footer .brand .brand-dot{width:50px;height:50px}
.f-col{position:absolute;top:190px;color:#fff;font-size:11px;line-height:16px}
.f-col h5{color:var(--mint);font-size:12px;font-weight:600;margin-bottom:12px}
.f-row{display:flex;gap:8px;margin-bottom:6px}
.f-col.contact{left:150px;width:200px}
.f-col.links{left:395px}
.f-col.links a{display:block;color:#fff;text-decoration:none;margin-bottom:7px}
.f-col.links a.active{text-decoration:underline}
.map{position:absolute;left:536px;top:182px;width:188px;height:136px;border-radius:12px;background:linear-gradient(135deg,#eef0ee,#dfe6e8)}
.inquiry{position:absolute;left:786px;top:54px;width:262px;height:278px;background:var(--mint);border-radius:36px;padding:26px 24px 0}
.inquiry h5{text-align:center;color:var(--ink);font-size:13px;font-weight:600;margin-bottom:10px}
.field{border-bottom:1px solid #b4dcca;color:#5f7f73;font-size:9.5px;padding:12px 0 6px}
.field.tall{padding-top:18px}
.submit{display:block;margin:22px auto 0;width:82px;height:26px;background:var(--navy);color:#fff;font-size:11px;font-weight:500;text-align:center;line-height:26px;border-radius:4px}
.copyright{position:absolute;left:150px;top:370px;color:#fff;font-size:10px}
.socials{position:absolute;left:743px;top:364px;display:flex;gap:12px}
.socials span{width:20px;height:20px;border-radius:50%;background:#fff}
.socials span:first-child{background:var(--mint)}
</style>
</head>
<body>

<header class="section hero">
  <div class="hero-photo" role="img" aria-label="Modern glass office building at dusk with landscaped planters"></div>
  <nav class="nav">
    <div class="brand"><span class="brand-dot"></span>Velloway Advisory</div>
    <div class="nav-links">
      <span class="active">Home</span><span>About Us</span><span>Services</span><span>Team</span><span>Contact Us</span>
    </div>
    <div class="btn-inquiry">Inquiry Now</div>
  </nav>
  <div class="hero-card">
    <h1>BUILDING<br>SUCCESS</h1>
    <div class="sub">in Southern<br>California</div>
    <div class="tag">Expertise at Every Step:<b>From Planning to Execution</b></div>
  </div>
</header>

<section class="section who">
  <div class="eyebrow">WHO WE ARE</div>
  <p>At Velloway, we blend innovative strategies with local market expertise to guide your commercial real estate ventures. Whether you're launching a new restaurant, investing in retail spaces, or expanding a franchise, our dedicated team is here to turn your real estate aspirations into tangible success. Dive into a partnership that grows with you.</p>
  <hr>
</section>

<section class="section about">
  <div class="about-mark" aria-hidden="true"></div>
  <div class="about-name">Velloway Advisory</div>
  <div class="about-copy">
    <div class="h2">ABOUT US</div>
    <h3>Welcome to Velloway Advisory, your trusted partner in navigating the complexities of the real estate and small business markets.</h3>
    <p>Founded by industry veterans Marco Delvane and Kevin Arlo, we specialize in providing comprehensive services tailored to the unique needs of our clients. Whether you're a franchisee, a new restaurant owner, or a commercial real estate investor, our expertise in due diligence, construction management, and investment property evaluation ensures you make informed, strategic decisions.</p>
    <p>At Velloway Advisory, we are committed to your success. Our approach combines meticulous analysis, strategic insights, and personalized service to help you achieve your business goals. We pride ourselves on our ability to deliver results that exceed expectations, fostering long-term relationships built on trust and excellence.</p>
    <p>Discover how Velloway Advisory can support your business journey. Partner with us and experience the difference our dedication and expertise can make.</p>
  </div>
</section>

<section class="section services">
  <div class="services-band"></div>
  <div class="services-photo" role="img" aria-label="Hand stacking wooden blocks printed with storefronts into a pyramid"></div>
  <div class="services-copy">
    <div class="h2">OUR SERVICES</div>
    <div class="tabs">
      <div class="tab on">
        <div class="icon-box"><svg width="26" height="26" viewBox="0 0 26 26" fill="none" stroke="#1d2833" stroke-width="1.6"><rect x="2" y="2" width="8" height="7"/><rect x="16" y="2" width="8" height="7"/><rect x="9" y="17" width="8" height="7"/><path d="M6 9v4h14V9M13 13v4"/></svg></div>
        Including franchise development
      </div>
      <div class="tab">
        <div class="icon-box"><svg width="26" height="26" viewBox="0 0 26 26" fill="none" stroke="#1d2833" stroke-width="1.8"><circle cx="11" cy="11" r="7"/><path d="M16 16l7 7M8 11l2 2 4-4"/></svg></div>
        Due diligence
      </div>
      <div class="tab">
        <div class="icon-box"><svg width="26" height="26" viewBox="0 0 26 26" fill="none" stroke="#1d2833" stroke-width="1.6"><rect x="3" y="6" width="12" height="17"/><path d="M6 10h2M10 10h2M6 14h2M10 14h2M6 18h2M10 18h2M18 23V10l5 3v10"/></svg></div>
        Construction management
      </div>
    </div>
    <p>At Velloway Advisory, our Franchise Development &amp; Launch service is designed to transform your successful business into a thriving franchise. We start by thoroughly evaluating your business model to determine its franchisability. Once confirmed, our team handles every aspect of the franchise setup, including legal documentation, branding, marketing strategies, operational guidelines, and franchisee recruitment.</p>
    <p>Our goal is to ensure a seamless and efficient transition from a single successful location to a robust franchise network, empowering your business to scale effectively and achieve exponential growth. Partner with us to turn your business into a nationwide brand.</p>
  </div>
</section>

<section class="section team">
  <div class="h2">OUR TEAM</div>
  <article class="card one">
    <div class="avatar" role="img" aria-label="Portrait photo of principal Kevin Arlo"></div>
    <div class="card-body">
      <h4>Kevin Arlo</h4>
      <div class="role">Principal</div>
      <p>Kevin Arlo is a seasoned real estate expert with extensive experience in project and construction management, and a licensed real estate agent in California. Fluent in both English and Korean,...</p>
    </div>
    <div class="contact-icons">
      <span class="ci"><svg width="10" height="10" viewBox="0 0 10 10"><path d="M2 1l2 2-1 1.2a6 6 0 0 0 2.8 2.8L7 6l2 2-1.2 1.2C4 9 1 6 .8 2.2z" fill="#222"/></svg></span>
      <span class="ci"><svg width="10" height="8" viewBox="0 0 10 8"><rect width="10" height="8" rx="1" fill="#222"/><path d="M0 1l5 3.5L10 1" stroke="#fff" fill="none"/></svg></span>
      <span class="ci"><svg width="10" height="8" viewBox="0 0 10 8" fill="none" stroke="#222" stroke-width="1.2"><path d="M0 4h9M6 1l3 3-3 3"/></svg></span>
    </div>
  </article>
  <article class="card two">
    <div class="avatar" role="img" aria-label="Portrait photo of principal Marco Delvane"></div>
    <div class="card-body">
      <h4>Marco Delvane</h4>
      <div class="role">Principal</div>
      <p>Marco Delvane brings almost 20 years of rich experience as a real estate investor and a pivotal role at one of southern California's largest real estate management firms, where he...</p>
    </div>
    <div class="contact-icons">
      <span class="ci"><svg width="10" height="10" viewBox="0 0 10 10"><path d="M2 1l2 2-1 1.2a6 6 0 0 0 2.8 2.8L7 6l2 2-1.2 1.2C4 9 1 6 .8 2.2z" fill="#222"/></svg></span>
      <span class="ci"><svg width="10" height="8" viewBox="0 0 10 8"><rect width="10" height="8" rx="1" fill="#222"/><path d="M0 1l5 3.5L10 1" stroke="#fff" fill="none"/></svg></span>
      <span class="ci hot"><svg width="10" height="8" viewBox="0 0 10 8" fill="none" stroke="#fff" stroke-width="1.2"><path d="M0 4h9M6 1l3 3-3 3"/></svg></span>
    </div>
  </article>
</section>

<section class="section cta">
  <div class="cta-photo" role="img" aria-label="Glass and brick office towers against a blue sky"></div>
  <div class="cta-copy">
    <h2>UNLOCK YOUR BUSINESS<br>POTENTIAL TODAY!</h2>
    <p>At Velloway Advisory, we're dedicated to turning your business aspirations into reality. Our expertise and commitment ensure you make informed, strategic decisions that drive success. Take the first step towards achieving your goals with confidence.</p>
    <span class="btn-dark">Get Started Now</span>
  </div>
</section>

<footer class="section footer">
  <div class="footer-inner">
    <div class="brand"><span class="brand-dot"></span>Velloway Advisory</div>
    <div class="f-col contact">
      <h5>CONTACT US</h5>
      <div class="f-row"><svg width="11" height="11" viewBox="0 0 10 10"><path d="M2 1l2 2-1 1.2a6 6 0 0 0 2.8 2.8L7 6l2 2-1.2 1.2C4 9 1 6 .8 2.2z" fill="#fff"/></svg>555 010 2468</div>
      <div class="f-row"><svg width="11" height="9" viewBox="0 0 10 8"><rect width="10" height="8" rx="1" fill="#fff"/><path d="M0 1l5 3.5L10 1" stroke="#243342" fill="none"/></svg>info@vellowayadvisory.example</div>
      <div class="f-row"><svg width="11" height="13" viewBox="0 0 10 13"><path d="M5 0a5 5 0 0 1 5 5c0 3.5-5 8-5 8S0 8.5 0 5a5 5 0 0 1 5-5z" fill="#fff"/><circle cx="5" cy="5" r="2" fill="#243342"/></svg><span>Lorem Ipsum<br>12 Harbor Lane, Westfield<br>Park</span></div>
    </div>
    <div class="f-col links">
      <h5>QUICK LINK</h5>
      <a class="active">Home</a><a>About Us</a><a>Services</a><a>Team</a><a>Contact Us</a>
    </div>
    <div class="map" role="img" aria-label="Street map showing the office location"></div>
    <form class="inquiry">
      <h5>QUICK INQUIRY</h5>
      <div class="field">Name</div>
      <div class="field">Email</div>
      <div class="field">Phone</div>
      <div class="field tall">Comments</div>
      <span class="submit">Submit</span>
    </form>
    <div class="copyright">© 2024 Velloway Advisory. all right reserved</div>
    <div class="socials"><span></span><span></span><span></span></div>
  </div>
</footer>

</body>
</html>
```